Dog Grooming Provisions - Coat Revival Mist *

We are Moss Hollow Meadows. A city dog's country camp. We are a dog services company providing a camp experience in Upstate NY to the dogs of NYC. We are creating a hand made Coat Revival Mist for our clients (who are dogs!) for the holidays.
These labels will be used on a 4 ounce vintage style spray bottles. The design should have a vintage grooming provisions feel. We'd like to see the design be a simple, vintage style black with white, charcoal, or very dark almost black green.
The design should incorporate our varying vintage fonts, our logo with "grooming provisions" all natural & handmade, Coat Revive
Obviously this is a gift and while Coat Revive is important, our brand should be a focus. Perhaps a very simple and "elegant" bone but steer away from paws and pet cheesy! Classic, vintage and camp.

Target Market(s)

Upscale Pet Owners of NYC

Industry/Entity Type

Pet Care

Logo Text

Moss Hollow Meadows Dog Camp (Dog Camp is is for logo not necessary for label)

Font styles to use
Serif
Sans Serif
Script

Colors
9bcb3b
000000
5c5c5c

Requirements
Must have
• I am looking for a black and white or very simple design. I'd even like our logo for this use be black/white (if possible? - not sure if that can happen?)
• Our branding! Simple vintage feel.
• Grooming Provisions
• Coat Revival or Coat Revive or Coat Bright Mist
• Handmade
• All Natural
• Fonts of vintage style - varying with simple and bold (i attached some photos)
Nice to have
• **MAYBE a very Simple Bone (see drawing) - very very thin.
Should not have
• 1. PAWS or cheap looking dog related items
• 2. No bright colors - truly prefer black and white or black with intention to print on plain pulp/brown paper (attached photo)
• 3. Over designed

```html
<!DOCTYPE html>
<html lang="en">
<head>
<meta charset="utf-8">
<title>Coat Revive Label</title>
<link href="https://fonts.googleapis.com/css2?family=Bebas+Neue&family=Oswald:wght@400;500&display=swap" rel="stylesheet">
<style>
  :root {
    --page: #ffffff;
    --label: #141414;
    --ink: #e9e9e9;
    --ink-soft: #bdbdbd;
  }
  * { margin: 0; padding: 0; box-sizing: border-box; }
  html, body { width: 1200px; height: 857px; overflow: hidden; background: var(--page); }
  .canvas {
    width: 1200px; height: 857px;
    display: flex; align-items: center; justify-content: center;
  }
  .label {
    position: relative;
    width: 560px; height: 780px;
    background: var(--label);
    color: var(--ink);
    display: flex; flex-direction: column; align-items: center;
    font-family: "Oswald", sans-serif;
  }
  .border-rule {
    position: absolute; left: 0; right: 0; height: 22px;
    border-top: 6px solid var(--ink);
    border-bottom: 2px solid var(--ink);
  }
  .border-rule.top { top: 18px; }
  .border-rule.bottom { bottom: 18px; }
  .brand {
    margin-top: 92px;
    width: 250px; height: 250px;
    border: 4px solid var(--ink-soft);
    border-radius: 50%;
    display: flex; align-items: center; justify-content: center;
    text-align: center;
    font-weight: 400; font-size: 34px; line-height: 1.15;
    letter-spacing: 2px; text-transform: uppercase;
    color: var(--ink);
  }
  .product-name {
    margin-top: 30px;
    font-family: "Bebas Neue", sans-serif;
    font-size: 118px; line-height: 1;
    letter-spacing: 3px;
    color: var(--ink);
  }
  .handmade {
    display: flex; align-items: center; gap: 14px;
    margin-top: 8px;
    font-size: 30px; letter-spacing: 9px; font-weight: 500;
  }
  .rule-arrow { width: 110px; height: 14px; }
  .provisions {
    display: flex; align-items: center; gap: 14px;
    margin-top: 22px;
    font-size: 30px; letter-spacing: 2px; font-weight: 500;
    text-transform: uppercase;
  }
  .bone { width: 52px; height: 14px; }
  .divider { width: 330px; height: 2px; background: var(--ink); margin-top: 14px; }
  .detail {
    margin-top: 18px;
    font-size: 28px; letter-spacing: 3px; font-weight: 500;
    text-transform: uppercase;
  }
  .detail + .detail { margin-top: 10px; }
</style>
</head>
<body>
  <main class="canvas">
    <section class="label">
      <div class="border-rule top"></div>

      <div class="brand">Moss<br>Hollow<br>Meadows</div>

      <h1 class="product-name">COAT REVIVE</h1>

      <div class="handmade">
        <svg class="rule-arrow" viewBox="0 0 110 14" aria-hidden="true">
          <line x1="0" y1="7" x2="104" y2="7" stroke="#e9e9e9" stroke-width="2"/>
          <path d="M96 2 L106 7 L96 12" fill="none" stroke="#e9e9e9" stroke-width="2"/>
        </svg>
        <span>HANDMADE</span>
        <svg class="rule-arrow" viewBox="0 0 110 14" aria-hidden="true">
          <line x1="6" y1="7" x2="110" y2="7" stroke="#e9e9e9" stroke-width="2"/>
          <path d="M14 2 L4 7 L14 12" fill="none" stroke="#e9e9e9" stroke-width="2"/>
        </svg>
      </div>
      <div class="divider"></div>

      <div class="provisions">
        <span>Grooming</span>
        <svg class="bone" viewBox="0 0 52 14" aria-hidden="true">
          <line x1="8" y1="7" x2="44" y2="7" stroke="#e9e9e9" stroke-width="3"/>
          <circle cx="5" cy="3.5" r="3.5" fill="#e9e9e9"/>
          <circle cx="5" cy="10.5" r="3.5" fill="#e9e9e9"/>
          <circle cx="47" cy="3.5" r="3.5" fill="#e9e9e9"/>
          <circle cx="47" cy="10.5" r="3.5" fill="#e9e9e9"/>
        </svg>
        <span>Provisions</span>
      </div>

      <p class="detail">• EST 2005 •</p>
      <p class="detail">• All Natural •</p>

      <div class="border-rule bottom"></div>
    </section>
  </main>
</body>
</html>
```